Book Cover Design Project

Hello,

I am looking to get a cover created for my book.

Size 6 X 9

Title:
Quiet Ledger Steady Gains

Sub-Title:
Plain Methods for Growing Steady Gains Within Your Quiet Ledger

Author:
Martin Fenwick

The book could have an image or only typography.

If it does include an image do not use an image of a real person. If you use a person, he can be shaded in, outlined, etc

I like the color white and blue however, I am open to other colors as well.

Below is the cover of my previous book that has an image:
http://www.quillmarket.example/Dawn-Of-Stag-Path-Vowed-Final/dp/284610375K/ref=sr_1_1?ie=UTF8&s=books&qid=2417307529&sr=1-1

I like simple designs but open to other concepts also

attached is the text to be used for the back of the book.

Thank you in advance for your designs,

Target Market(s)

This book will be for small business owners. Typically males/females between the age of 25 - 45 looking to make more money without going broke with marketing.

Industry/Entity Type

Business

Requirements
Must have
• Must include the Title, Subtitle and Author on the cover

Nice to have
• An image that represents a small business growing
Should not have
• Images of a real person. Stylized versions are ok.

```html
<!DOCTYPE html>
<html lang="en">
<head>
<meta charset="utf-8">
<title>Quiet Ledger Steady Gains — Book Cover</title>
<link href="https://fonts.googleapis.com/css2?family=Poiret+One&family=Quicksand:wght@400&family=Antic&display=swap" rel="stylesheet">
<style>
  :root {
    --bg: #ececec;
    --paper: #fbfbfb;
    --ink: #1d1d1d;
    --ink-soft: #3a3a3a;
    --blue: #0d9ed8;
    --blue-light: #5cc0e8;
  }
  html, body {
    margin: 0;
    width: 1200px;
    height: 900px;
    overflow: hidden;
    background: var(--bg);
  }
  .stage {
    width: 1200px;
    height: 900px;
    display: flex;
    align-items: center;
    justify-content: center;
  }
  .cover {
    position: relative;
    width: 560px;
    height: 840px;
    background: var(--paper);
    box-sizing: border-box;
    border-bottom: 10px solid var(--blue);
    display: flex;
    flex-direction: column;
    align-items: center;
  }
  .title-block {
    margin-top: 62px;
    width: 480px;
    display: flex;
    flex-direction: column;
    align-items: center;
  }
  .title-top {
    display: flex;
    align-items: center;
    width: 100%;
    gap: 18px;
  }
  .title-top .rule { flex: 1; height: 2px; background: var(--blue); }
  .title-small {
    font-family: "Poiret One", sans-serif;
    font-size: 24px;
    letter-spacing: 1px;
    color: var(--ink);
    text-transform: uppercase;
    white-space: nowrap;
  }
  .title-large {
    font-family: "Poiret One", sans-serif;
    font-size: 70px;
    line-height: 1;
    margin-top: 2px;
    color: var(--ink);
    text-transform: uppercase;
    white-space: nowrap;
  }
  .title-rule {
    width: 100%;
    height: 2px;
    background: var(--blue);
    margin-top: 8px;
  }
  .subtitle {
    margin-top: 18px;
    width: 420px;
    font-family: "Quicksand", sans-serif;
    font-size: 14px;
    line-height: 1.25;
    letter-spacing: 0.5px;
    text-align: center;
    text-transform: uppercase;
    color: var(--ink-soft);
  }
  .illustration {
    margin-top: 70px;
    width: 200px;
    height: 400px;
    border-radius: 100px 100px 40px 40px;
    background: linear-gradient(180deg, var(--blue-light) 0%, var(--blue) 100%);
  }
  .author {
    position: absolute;
    bottom: 46px;
    font-family: "Antic", sans-serif;
    font-size: 24px;
    letter-spacing: 1px;
    color: var(--ink-soft);
    text-transform: uppercase;
  }
</style>
</head>
<body>
  <main class="stage">
    <article class="cover">
      <header class="title-block">
        <div class="title-top">
          <span class="rule"></span>
          <span class="title-small">Quiet Ledger</span>
          <span class="rule"></span>
        </div>
        <h1 class="title-large" style="margin-bottom:0;font-weight:400">Steady Gains</h1>
        <div class="title-rule"></div>
      </header>
      <p class="subtitle">Plain Methods for Growing Steady Gains Within Your Quiet Ledger</p>
      <div class="illustration" role="img" aria-label="Stylised blue fish stacked from tiny to large, suggesting a small business growing"></div>
      <p class="author">Martin Fenwick</p>
    </article>
  </main>
</body>
</html>
```